TallyNest Webpages and Logo

See attached brief. Take the existing website www.tallynest.co.uk and logo and transform these assets to:

Give people who arrive on the site for first time the confidence to sign-up easily and quickly
Allow regular returning users quick and easy placing of predictions and encourage them to share the TallyNest prediction on social networks and with their contacts
Convey the essence of a community working together to enjoyably come-up with smart predictions on sporting events
Work seamlessly and well across smartphones, tablets and desktop i.e. Should be Responsive Web Design
Updates

Target Market(s)

Users are sports fans with opinions
Primarily male and early twenties to mid-thirties
They are competitive - they want to beat their peers
Many are from outside the UK

Industry/Entity Type

Events

Logo Text

TallyNest

Coding

Coded - Design and coding required

Number of Pages Required

4 page

Font styles to use
Sans Serif

Requirements
Must have
• Responsive Web Design
• Mobile First
• HTML must work with dedicated bespoke application developed in ASP.NET using MS SQL underneath
• See Brief
Nice to have
• See brief
Should not have
• See brief

```html
<!DOCTYPE html>
<html lang="en">
<head>
<meta charset="utf-8">
<title>TallyNest – Predict scores</title>
<link href="https://fonts.googleapis.com/css2?family=Open+Sans:wght@400;600;700&family=Lora&display=swap" rel="stylesheet">
<style>
:root{
  --blue:#2b8ac0;
  --blue-dark:#1f6f9e;
  --blue-text:#3a95c4;
  --pink:#e0316f;
  --black:#000;
  --light:#f2f2f2;
  --grey-text:#8c8c8c;
  --footer:#4b4b4b;
  --footer-text:#d8d8d8;
  --white:#fff;
}
*{box-sizing:border-box;margin:0;padding:0}
html,body{width:779px;height:1200px;overflow:hidden;background:var(--white)}
body{position:relative;font-family:"Open Sans",sans-serif;color:#222}
.abs{position:absolute}

/* top bar */
.topbar{left:0;top:0;width:779px;height:32px;background:var(--white)}
.kitty{left:39px;top:9px;font-size:10px;color:var(--blue-text)}
.kitty .rise{color:#3a9a3a;font-size:8px;font-weight:700}
.btn-top{top:6px;height:20px;width:74px;background:var(--blue);color:var(--white);font-size:10px;text-align:center;line-height:20px;border:1px solid var(--blue-dark);border-radius:2px}

/* nav */
.nav{left:0;top:32px;width:779px;height:54px;background:var(--black)}
.brand{left:39px;top:40px;display:flex;align-items:center;gap:7px}
.brand-dot{width:34px;height:34px;border-radius:50%;background:var(--blue)}
.brand-name{color:var(--white);font-size:18px;font-weight:700}
.menu{left:298px;top:52px;display:flex;gap:0;font-size:10px;color:var(--white)}
.menu span{margin-right:30px}

/* hero */
.hero{left:0;top:86px;width:779px;height:348px;background:radial-gradient(ellipse at 75% 40%,#2f5f8c 0%,#1d3550 35%,#0c1520 70%),#0b1018}
.hero-grass{left:0;top:330px;width:779px;height:104px;background:linear-gradient(180deg,rgba(40,80,30,0) 0%,#2b4a1f 60%,#24401a 100%)}
.hero-title{left:0;top:118px;width:779px;text-align:center;color:var(--white);font-size:24px;line-height:35px}
.hero-title .prize{color:var(--pink);font-weight:700}
.hero-sub{left:100px;top:189px;width:579px;text-align:center;color:var(--white);font-family:"Lora",serif;font-size:10px;line-height:15px;text-transform:uppercase}
.join{left:325px;top:232px;width:150px;height:39px;background:var(--blue);border:1px solid #5fb3de;color:var(--white);font-size:17px;font-weight:700;text-align:center;line-height:37px;border-radius:2px}
.arrow{top:252px}

/* tips */
.tips{left:120px;top:291px;width:554px;height:102px;border:1px solid #cfcfcf}
.tips-head{position:absolute;left:0;top:0;width:552px;height:33px;background:var(--white)}
.tips-title{position:absolute;left:57px;top:7px;font-size:14px;font-style:italic;color:var(--blue);font-weight:600}
.social-pill{position:absolute;top:10px;height:14px;font-size:7px;line-height:14px;padding:0 4px;border-radius:2px}
.pill-blue{background:#3a77c0;color:var(--white);font-weight:700}
.pill-count{background:var(--white);border:1px solid #ccc;color:#333;line-height:12px}
.tips-body{position:absolute;left:0;top:33px;width:552px;height:67px;background:rgba(140,140,140,.85);display:flex}
.tip{flex:1;text-align:center;color:var(--white)}
.tip.mid{background:rgba(190,190,190,.55)}
.tip h4{font-size:12px;font-weight:400;color:#111;margin-top:8px;letter-spacing:.3px}
.tip h4 b{margin-left:18px;font-weight:600}
.tip p{font-size:8px;line-height:15.5px;margin-top:2px}
.tip.mid p{color:var(--blue)}

/* features */
.features{left:39px;top:420px;width:700px;height:102px;background:var(--white);box-shadow:0 2px 6px rgba(0,0,0,.25);display:flex}
.feature{flex:1;display:flex;padding:22px 0 0 21px;border-right:1px solid #e2e2e2}
.feature:last-child{border-right:0}
.feature-icon{width:52px;height:52px;background:linear-gradient(160deg,#3aa0d6,#1d6f9e);border-radius:3px;flex-shrink:0}
.feature-text{margin-left:10px}
.feature-text h3{font-size:14px;font-weight:400;color:#111;margin-top:-3px}
.feature-text p{font-size:7.5px;line-height:15px;color:var(--grey-text);margin-top:2px;width:140px}

/* matches */
.section-title{left:0;top:543px;width:779px;text-align:center;font-size:14px;font-weight:700;color:var(--blue)}
.match{width:225px;height:178px}
.match-body{height:141px;background:var(--light);position:relative}
.crest{position:absolute;top:26px;width:60px;height:60px;border-radius:50%;background:var(--white)}
.crest i{position:absolute;left:16px;top:12px;width:28px;height:34px;border-radius:4px 4px 14px 14px}
.vs{position:absolute;left:0;width:225px;top:48px;text-align:center;font-size:13px}
.team{position:absolute;top:96px;font-size:10px;color:var(--blue-text)}
.kick{position:absolute;top:117px;left:0;width:225px;text-align:center;font-size:8px;color:#111}
.kick svg{vertical-align:-2px;margin-right:6px}
.predict{height:37px;background:var(--blue);color:var(--white);font-size:13px;font-weight:700;text-align:center;line-height:37px}
.show-all{left:0;top:992px;width:779px;text-align:center;font-size:12px;color:var(--blue-text)}

/* footer */
.footer{left:0;top:1027px;width:779px;height:173px;background:var(--footer)}
.foot-col h5{font-size:11.5px;font-weight:400;color:var(--blue-text);letter-spacing:.3px}
.foot-col ul{list-style:none;margin-top:5px}
.foot-col li{font-size:7.5px;line-height:10.8px;color:var(--footer-text)}
.feedback{left:294px;top:1048px;width:189px;height:31px;border:1px solid var(--blue-text);color:var(--blue-text);font-size:10.5px;text-align:center;line-height:29px}
.feedback svg{vertical-align:-2px;margin-right:10px}
.soc{top:1102px;width:25px;height:25px;background:#2d2d2d;border-radius:2px}
.pundit-title{left:559px;top:1045px;font-size:11.5px;color:var(--blue-text);letter-spacing:.3px}
.pundit-photo{left:601px;top:1068px;width:51px;height:51px;border-radius:50%;background:linear-gradient(160deg,#dcdcdc,#8a8a8a);border:2px solid var(--white)}
.pundit-quote{left:535px;top:1121px;width:190px;font-size:7.5px;line-height:13px;color:var(--footer-text)}
.pundit-by{left:649px;top:1146px;font-size:9.5px;color:var(--white)}
.copyright{left:0;top:1172px;width:779px;text-align:center;font-size:6.5px;color:var(--footer-text)}
</style>
</head>
<body>

<div class="abs topbar"></div>
<div class="abs kitty">Kitty: £1289 <span class="rise">▲5%</span></div>
<div class="abs btn-top" style="left:586px">Login</div>
<div class="abs btn-top" style="left:665px">Register</div>

<div class="abs nav"></div>
<div class="abs brand"><span class="brand-dot"></span><span class="brand-name">TallyNest</span></div>
<nav class="abs menu"><span>Home</span><span>About Us</span><span>Tables</span><span>Kitty</span><span>FAQ</span><span>History</span><span>Contact</span></nav>

<div class="abs hero" role="img" aria-label="Blurred action photo of a footballer striking a ball in a floodlit stadium"></div>
<div class="abs hero-grass"></div>
<div class="abs hero-title">Predict 6 scores<br>to win <span class="prize">£250,000</span></div>
<div class="abs hero-sub">Maecenas a sapien tortor quis tincidunt lectus. Donec ullamcorper dui sit amet lorem ultrices sed porttitor massa eu dui scelerisque</div>
<div class="abs join">JOIN NOW</div>
<svg class="abs arrow" style="left:39px" width="10" height="14" viewBox="0 0 10 14"><path d="M8 1L2 7l6 6" fill="none" stroke="#9aa3ad" stroke-width="2"/></svg>
<svg class="abs arrow" style="left:731px" width="10" height="14" viewBox="0 0 10 14"><path d="M2 1l6 6-6 6" fill="none" stroke="#9aa3ad" stroke-width="2"/></svg>

<section class="abs tips">
  <div class="tips-head">
    <div class="tips-title">TallyNest Hot Tips!!</div>
    <span class="social-pill pill-blue" style="left:237px">Follow @ScoreWatch</span>
    <span class="social-pill pill-count" style="left:333px">451K followers</span>
    <span class="social-pill pill-blue" style="left:404px">Like</span>
    <span class="social-pill pill-blue" style="left:443px">Share</span>
    <span class="social-pill pill-count" style="left:474px">65k</span>
  </div>
  <div class="tips-body">
    <div class="tip"><h4>RESULT<b>100%</b></h4><p>NORTHGATE UNITED WIN</p></div>
    <div class="tip mid"><h4>SCORE<b>50%</b> <span style="color:var(--blue);font-size:9px">▼</span></h4><p>ELMFORD VILLA 0<br>NORTHGATE UNITED 2<br>NORTHGATE</p></div>
    <div class="tip"><h4>1st GOAL<b>80%</b></h4><p>DALTON R</p></div>
  </div>
</section>

<section class="abs features">
  <div class="feature"><div class="feature-icon" role="img" aria-label="Puzzle piece icon"></div><div class="feature-text"><h3>Predict</h3><p>Maecenas a sapien tortor quis tincidt lectus. Donec ullamcorper dui sit am lorem ultrices sed......»</p></div></div>
  <div class="feature"><div class="feature-icon" role="img" aria-label="Light bulb icon"></div><div class="feature-text"><h3>Get Tips</h3><p>Maecenas a sapien tortor quis tincidt lectus. Donec ullamcorper dui sit am ultrices sed......»</p></div></div>
  <div class="feature"><div class="feature-icon" role="img" aria-label="Treasure chest icon"></div><div class="feature-text"><h3>Win</h3><p>Maecenas a sapien tortor quis tincidt lectus. Donec ullamcorper dui sit am ultrices sed......»</p></div></div>
</section>

<h2 class="abs section-title">TEMPOR INCIDIDUNT</h2>

<!-- fixtures -->
<div class="abs match" style="left:39px;top:582px"><div class="match-body"><span class="crest" style="left:27px"><i style="background:#9fc9e6"></i></span><div class="vs">V</div><span class="crest" style="left:134px"><i style="background:#2d4fa0"></i></span><span class="team" style="left:18px">Northgate City</span><span class="team" style="left:131px">Glass Harbour</span><div class="kick"><svg width="9" height="9" viewBox="0 0 10 10"><circle cx="5" cy="5" r="4" fill="none" stroke="#2b8ac0" stroke-width="1.5"/><path d="M5 3v2h2" stroke="#2b8ac0" fill="none"/></svg>Sat 20 Dec 2014 12:45 PM</div></div><div class="predict">Predict Score Now!</div></div>
<div class="abs match" style="left:277px;top:582px"><div class="match-body"><span class="crest" style="left:27px"><i style="background:#1e3f8f"></i></span><div class="vs">V</div><span class="crest" style="left:134px"><i style="background:#d3202a"></i></span><span class="team" style="left:18px">Northgate City</span><span class="team" style="left:131px">Glass Harbour</span><div class="kick"><svg width="9" height="9" viewBox="0 0 10 10"><circle cx="5" cy="5" r="4" fill="none" stroke="#2b8ac0" stroke-width="1.5"/><path d="M5 3v2h2" stroke="#2b8ac0" fill="none"/></svg>Sat 20 Dec 2014 12:45 PM</div></div><div class="predict">Predict Score Now!</div></div>
<div class="abs match" style="left:514px;top:582px"><div class="match-body"><span class="crest" style="left:27px"><i style="background:#6b2a4a"></i></span><div class="vs">V</div><span class="crest" style="left:134px"><i style="background:#8cc6e8"></i></span><span class="team" style="left:18px">Northgate City</span><span class="team" style="left:131px">Glass Harbour</span><div class="kick"><svg width="9" height="9" viewBox="0 0 10 10"><circle cx="5" cy="5" r="4" fill="none" stroke="#2b8ac0" stroke-width="1.5"/><path d="M5 3v2h2" stroke="#2b8ac0" fill="none"/></svg>Sat 20 Dec 2014 12:45 PM</div></div><div class="predict">Predict Score Now!</div></div>

<div class="abs match" style="left:39px;top:797px"><div class="match-body"><span class="crest" style="left:27px"><i style="background:#9fc9e6"></i></span><div class="vs">V</div><span class="crest" style="left:134px"><i style="background:#2d4fa0"></i></span><span class="team" style="left:18px">Northgate City</span><span class="team" style="left:131px">Glass Harbour</span><div class="kick"><svg width="9" height="9" viewBox="0 0 10 10"><circle cx="5" cy="5" r="4" fill="none" stroke="#2b8ac0" stroke-width="1.5"/><path d="M5 3v2h2" stroke="#2b8ac0" fill="none"/></svg>Sat 20 Dec 2014 12:45 PM</div></div><div class="predict">Predict Score Now!</div></div>
<div class="abs match" style="left:277px;top:797px"><div class="match-body"><span class="crest" style="left:27px"><i style="background:#9fc9e6"></i></span><div class="vs">V</div><span class="crest" style="left:134px"><i style="background:#2d4fa0"></i></span><span class="team" style="left:18px">Northgate City</span><span class="team" style="left:131px">Glass Harbour</span><div class="kick"><svg width="9" height="9" viewBox="0 0 10 10"><circle cx="5" cy="5" r="4" fill="none" stroke="#2b8ac0" stroke-width="1.5"/><path d="M5 3v2h2" stroke="#2b8ac0" fill="none"/></svg>Sat 20 Dec 2014 12:45 PM</div></div><div class="predict">Predict Score Now!</div></div>
<div class="abs match" style="left:514px;top:797px"><div class="match-body"><span class="crest" style="left:27px"><i style="background:#9fc9e6"></i></span><div class="vs">V</div><span class="crest" style="left:134px"><i style="background:#2d4fa0"></i></span><span class="team" style="left:18px">Northgate City</span><span class="team" style="left:131px">Glass Harbour</span><div class="kick"><svg width="9" height="9" viewBox="0 0 10 10"><circle cx="5" cy="5" r="4" fill="none" stroke="#2b8ac0" stroke-width="1.5"/><path d="M5 3v2h2" stroke="#2b8ac0" fill="none"/></svg>Sat 20 Dec 2014 12:45 PM</div></div><div class="predict">Predict Score Now!</div></div>

<div class="abs show-all">Show All &nbsp;<svg width="13" height="11" viewBox="0 0 13 11" style="vertical-align:-1px"><path d="M1 5h3v5H1zM4 5l3-4h1v3h4v2l-2 4H4" fill="none" stroke="#3a95c4" stroke-width="1.2"/></svg></div>

<footer class="abs footer"></footer>
<div class="abs foot-col" style="left:39px;top:1045px"><h5>USEFUL LINKS</h5><ul><li>Home</li><li>About Us</li><li>Tables</li><li>Kitty</li><li>FAQ</li><li>Profile</li><li>History</li><li>Mini-Liga Admin</li><li>Contact</li></ul></div>
<div class="abs foot-col" style="left:164px;top:1045px"><h5>HELP</h5><ul><li>Login</li><li>Register</li><li>Terms</li><li>Site Map</li><li>Privacy</li><li>Terms and Conditions</li></ul></div>
<div class="abs feedback"><svg width="11" height="9" viewBox="0 0 11 9"><rect x=".5" y=".5" width="10" height="8" fill="none" stroke="#3a95c4"/><path d="M.5.5l5 4 5-4" fill="none" stroke="#3a95c4"/></svg>Send Us Feedback</div>
<div class="abs soc" style="left:298px"><svg width="25" height="25" viewBox="0 0 25 25"><rect x="8" y="9" width="9" height="7" fill="#fff"/><path d="M8 9l4.5 4 4.5-4" fill="none" stroke="#2d2d2d"/></svg></div>
<div class="abs soc" style="left:329px"></div>
<div class="abs soc" style="left:360px"></div>
<div class="abs soc" style="left:392px"></div>
<div class="abs soc" style="left:423px"></div>
<div class="abs soc" style="left:455px"></div>
<div class="abs pundit-title">PUNDITS PREDICTIONS</div>
<div class="abs pundit-photo" role="img" aria-label="Portrait photo of the pundit"></div>
<div class="abs pundit-quote">Sed ut perspiciatis unde omnis iste natus error sit voluptatem &nbsp;doloremque.....</div>
<div class="abs pundit-by">By Ben Harlow</div>
<div class="abs copyright">Copyright © TallyNest 2014. All Rights Reserved.</div>

</body>
</html>
```